WP website design for Brevin

We need a wordpress design for an auction company. The winning design will incorporate a professional color scheme with company logo in a clean, image driven layout. The design needs to consider that this will be developed on a responsive theme. Colors are those that will highlight the logo.

Industry/Entity Type

It Company

Font styles to use
Serif
Sans Serif

Colors

Designer to choose colors to be used in the design.

Requirements
Must have
• Navigation: 1) Home 2) Auctions 3) Services 4) Real Estate 5 ) Previous Auctions 6) About Us 7) Contact Us

Sites referenced that client likes: https://www.pledgora.example/ and http://www.quillmoorbids.example/ as examples of image rich sites. There will be large slideshow element and 4 calls to action (with any stock images suitable) 1) Real Estate 2) Auctions 3) Liquidations 4) Appraisals

Content will also include text (below) and auctions as seen at http://www.quillmoorbids.example/ below the slideshow or as in the attached image.

Footer will have contact info, social icons (FB, Twitter, YT, RSS) and news posts widget

Colors will be that of the logo and any others to highlight/compliment the design.

Nice to have
• Use of dropdown menu styling

```html
<!DOCTYPE html>
<html lang="en">
<head>
<meta charset="utf-8">
<title>Brevin Auctions</title>
<link rel="stylesheet" href="https://fonts.googleapis.com/css2?family=Roboto+Slab:wght@300;400;700&family=Montserrat:wght@500;600;700&family=Open+Sans:ital,wght@0,400;0,600;1,400;1,600&display=swap">
<style>
:root{
  --navy:#0f2470;
  --navy-footer:#13296c;
  --navy-deep:#0c1f58;
  --ink:#1d1d1d;
  --grey-text:#7b7b7b;
  --panel:#e4e4e4;
  --red:#c8161d;
  --orange:#f5a41d;
  --gold:#f0c31c;
  --white:#ffffff;
}
*{box-sizing:border-box;margin:0;padding:0}
html,body{width:939px;height:1200px;overflow:hidden;background:var(--white)}
body{font-family:"Open Sans",Arial,sans-serif;color:var(--ink)}
.page{position:relative;width:939px;height:1200px;overflow:hidden}
.abs{position:absolute}

/* header */
.top-rule{left:0;top:0;width:939px;height:7px;background:var(--navy)}
.header-bg{left:0;top:7px;width:939px;height:503px;background:radial-gradient(ellipse at 50% 30%,#f2f2f2 0%,#dcdcdc 60%,#cfcfcf 100%)}
.brand{left:113px;top:36px;display:flex;align-items:center;gap:10px}
.brand-mark{width:14px;height:14px;background:var(--navy)}
.brand-name{font-family:"Open Sans",Arial,sans-serif;font-weight:600;font-size:24px;color:var(--navy)}
.social{left:700px;top:18px;display:flex;gap:4px}
.social span{width:30px;height:30px;border-radius:4px;background:var(--navy);display:block}
.social span:nth-child(2){background:#2b4a9a}
.social span:nth-child(3){background:#3c5bb0}
.social span:nth-child(4){background:#506cc0}

/* nav */
.main-nav{left:106px;top:97px;width:727px;height:29px;background:var(--navy)}
.main-nav a{position:absolute;top:8px;font-size:11px;color:var(--white);text-decoration:none}

/* slider */
.slider{left:106px;top:126px;width:727px;height:253px;background:linear-gradient(180deg,#e8edf3 0%,#d7dde5 35%,#a88466 55%,#8d735e 75%,#6f9a4a 92%,#5d8a3c 100%)}
.slide-arrow{top:229px;width:14px;height:16px}
.slide-dots{left:457px;top:364px;display:flex;gap:4px}
.slide-dots span{width:14px;height:9px;background:var(--white);border:1px solid #aaa;display:block}

/* calls to action */
.cta{top:387px;width:176px;height:117px;background:linear-gradient(135deg,#f4f4f4 0%,#dcdcdc 100%);border:1px solid #b9b9b9;overflow:hidden}
.cta-title{position:absolute;left:12px;top:5px;font-family:"Roboto Slab",Georgia,serif;font-size:17px;color:var(--navy);letter-spacing:.3px;white-space:nowrap}
.cta-text{position:absolute;left:12px;top:29px;width:98px;font-size:10px;line-height:13px;color:var(--ink)}
.cta-art{position:absolute;right:0;bottom:0;width:72px;height:86px}

/* welcome */
.welcome-title{left:121px;top:525px;font-family:"Roboto Slab",Georgia,serif;font-weight:300;font-size:23px;color:var(--navy)}
.welcome-text{left:121px;top:554px;width:698px;font-size:10.4px;line-height:14.4px;color:var(--grey-text)}

/* current auctions */
.section-title{left:121px;top:643px;font-family:"Roboto Slab",Georgia,serif;font-weight:300;font-size:23px;color:var(--navy);white-space:nowrap}
.section-rule{left:301px;top:661px;width:464px;height:2px;background:var(--navy)}
.pager{top:641px;width:25px;height:23px;background:var(--navy)}

.auction{top:676px;width:342px;height:212px;background:var(--panel);border-radius:4px;overflow:hidden}
.auction-head{position:absolute;left:0;top:0;width:100%;height:36px;background:var(--navy);color:var(--white);font-family:"Montserrat",Arial,sans-serif;font-weight:600;font-size:14.5px;letter-spacing:.4px;padding:9px 0 0 10px}
.auction-photo{position:absolute;left:6px;top:42px;width:154px;height:130px}
.auction-btn{position:absolute;top:177px;width:74px;height:30px;background:var(--navy);color:var(--white);font-size:11px;display:flex;align-items:center;justify-content:center;gap:5px}
.auction-btn i{display:block;width:11px;height:10px;background:var(--gold);border-radius:1px}
.auction-info{position:absolute;left:169px;top:42px;width:170px}
.lot-title{font-family:"Montserrat",Arial,sans-serif;font-weight:700;font-size:11.2px;line-height:14px;color:var(--navy);letter-spacing:.3px}
.lot-contact{margin-top:4px;font-family:"Montserrat",Arial,sans-serif;font-weight:500;font-size:9.6px;line-height:12.8px;color:var(--ink)}
.lot-live{font-family:"Montserrat",Arial,sans-serif;font-weight:700;font-size:10.6px;color:var(--red);letter-spacing:.3px}
.lot-detail{font-size:9.8px;line-height:13.5px;color:var(--ink)}
.lot-detail b{color:var(--navy);font-weight:600}
.bid-btn{margin-top:6px;width:163px;height:20px;border:1px solid var(--gold);border-radius:3px;background:var(--white);font-family:"Montserrat",Arial,sans-serif;font-weight:700;font-size:10.2px;color:var(--navy);display:flex;align-items:center;gap:8px;padding-left:8px}
.bid-btn i{display:block;width:16px;height:11px;background:#3b7fd9;border-radius:1px}

/* partners */
.partners{left:310px;top:906px;display:flex;gap:22px;align-items:center}
.partners span{display:block;background:#7a7a7a}

/* footer */
.footer{left:0;top:933px;width:939px;height:225px;background:var(--navy-footer)}
.content-tab{left:106px;top:930px;width:712px;height:18px;background:var(--white);border-radius:0 0 5px 5px}
.foot-title{top:966px;font-style:italic;font-weight:400;font-size:14px;color:var(--white)}
.site-menu{left:120px;top:984px;list-style:none}
.site-menu li{font-size:10.6px;color:var(--white);line-height:21.2px}
.col-divider{top:1008px;width:1px;height:128px;background:rgba(255,255,255,.12)}
.news{left:309px;width:240px;height:63px}
.news-photo{position:absolute;left:0;top:0;width:72px;height:63px}
.news-head{position:absolute;left:78px;top:-2px;font-size:10.4px;color:var(--orange)}
.news-text{position:absolute;left:78px;top:20px;width:160px;font-size:10.2px;line-height:13px;color:var(--white)}
.contact-row{left:657px;display:flex;gap:5px;font-size:10.2px;line-height:13px;color:var(--white)}
.contact-row svg{flex:none}
.foot-brand{left:660px;top:1100px;font-family:"Open Sans",Arial,sans-serif;font-weight:600;font-size:15px;color:var(--white);display:flex;align-items:center;gap:8px}
.foot-brand i{display:block;width:10px;height:10px;background:var(--white)}
.copyright-bar{left:0;top:1158px;width:939px;height:42px;background:var(--navy-deep);border-top:1px solid #2a3f86}
.copyright{left:0;top:1171px;width:939px;text-align:center;font-style:italic;font-size:10.6px;color:#e6e6e6}
</style>
</head>
<body>
<div class="page">

  <div class="abs top-rule"></div>
  <div class="abs header-bg"></div>

  <header>
    <div class="abs brand"><span class="brand-mark"></span><span class="brand-name">Brevin Auctions</span></div>
    <div class="abs social" aria-label="Social links">
      <span role="img" aria-label="Social link"></span>
      <span role="img" aria-label="Social link"></span>
      <span role="img" aria-label="Video channel"></span>
      <span role="img" aria-label="News feed"></span>
    </div>
  </header>

  <nav class="abs main-nav">
    <a style="left:14px">Home</a>
    <a style="left:83px">Auctions</a>
    <a style="left:164px">Services</a>
    <a style="left:243px">Real Estate</a>
    <a style="left:335px">Previous Auctions</a>
    <a style="left:459px">About Us</a>
    <a style="left:543px">Contact Us</a>
  </nav>

  <div class="abs slider" role="img" aria-label="Slideshow photo of a two-storey brick and siding family home with trees and lawn"></div>
  <svg class="abs slide-arrow" style="left:115px" viewBox="0 0 14 16"><path d="M10 2 L4 8 L10 14" fill="none" stroke="#333" stroke-width="2"/></svg>
  <svg class="abs slide-arrow" style="left:810px" viewBox="0 0 14 16"><path d="M4 2 L10 8 L4 14" fill="none" stroke="#333" stroke-width="2"/></svg>
  <div class="abs slide-dots"><span></span><span></span><span></span></div>

  <section aria-label="Services">
    <div class="abs cta" style="left:106px">
      <div class="cta-title">REAL ESTATE</div>
      <p class="cta-text">Lorem Ipsum roino gravida nibh veludi isd velit auctor aliq uet Aenean sollic udin, lorem quisbi udi ndum..</p>
      <div class="cta-art" role="img" aria-label="City tower buildings on a lawn" style="background:linear-gradient(180deg,#c7d6e6,#9fb3c4 60%,#6f9a4a)"></div>
    </div>
    <div class="abs cta" style="left:290px">
      <div class="cta-title">AUCTIONS</div>
      <p class="cta-text">Lorem Ipsum roin opitsoi gravida nibh veludi isd velit auctor aliq uet Aenean sollic udin lorem quisbi udi ndum..</p>
      <div class="cta-art" role="img" aria-label="Gavel over a sold stamp" style="background:linear-gradient(160deg,#e8e2dc,#c99a92 60%,#a8352e)"></div>
    </div>
    <div class="abs cta" style="left:473px">
      <div class="cta-title">LIQUIDATIONS</div>
      <p class="cta-text">Lorem Ipsum roino gravida nibh veludi isd velit auctor aliq uet Aenean sollic udin, lorem quisbi udi ndum..</p>
      <div class="cta-art" role="img" aria-label="Hand signing a document with a pen" style="background:linear-gradient(160deg,#e2e2e2,#bdbdbd 60%,#8a8a8a)"></div>
    </div>
    <div class="abs cta" style="left:656px">
      <div class="cta-title">APPRAISALS</div>
      <p class="cta-text">Lorem Ipsum roino gravida nibh veludi isd velit auctor aliq uet Aenean sollic udin, lorem quisbi udi ndum..</p>
      <div class="cta-art" role="img" aria-label="Small house model on appraisal papers" style="background:linear-gradient(160deg,#dfe6ee,#c9a978 60%,#8e7a5e)"></div>
    </div>
  </section>

  <main>
    <h1 class="abs welcome-title">Welcome to Brevin Auctions</h1>
    <p class="abs welcome-text">Lorem Ipsum. Proin gravida nibh vel velit auctor aliquet. Aenean sollicitudin, lorem quis bibendum auctor, nisi elit consequat ipsum, nec sagittis sem nibh id elit. Duis sed odio sit amet nibh vulputate cursus a sit amet mauris. Morbi accumsan ipsum velit. Nam nec tellus a odio tincidunt auctor a ornare odio. Sed non &nbsp;mauris vitae erat consequat auctor eu in elit. Class aptent taciti sociosqu ad litora torquent per conubia nostra, per inceptos himenaeos. Mauris in erat justo.</p>

    <h2 class="abs section-title">Cuttent Auctions</h2>
    <div class="abs section-rule"></div>
    <svg class="abs pager" style="left:765px" viewBox="0 0 25 23"><path d="M15 5 L9 11.5 L15 18" fill="none" stroke="#fff" stroke-width="2.5"/></svg>
    <svg class="abs pager" style="left:792px" viewBox="0 0 25 23"><path d="M10 5 L16 11.5 L10 18" fill="none" stroke="#fff" stroke-width="2.5"/></svg>

    <article class="abs auction" style="left:121px">
      <div class="auction-head">AUCTION TITLE WILL BE HERE</div>
      <div class="auction-photo" role="img" aria-label="Two-storey white house with lawn under a blue sky" style="background:linear-gradient(180deg,#9fc3e6 0%,#d9d4cc 45%,#b89c88 65%,#5f9a3d 100%)"></div>
      <div class="auction-btn" style="left:5px"><i></i>Details</div>
      <div class="auction-btn" style="left:85px"><i></i>Photos</div>
      <div class="auction-info">
        <div class="lot-title">4 BR / 1+ BA BRICK HOME<br>&amp; 0.630 ACRE LOT</div>
        <div class="lot-contact">DANA HOLLOWAY - ASHFORD<br>COUNTY CLERK &amp; MASTER<br>555-014-2287</div>
        <div class="lot-live" style="margin-top:20px">LIVE ON-SITE AUCTON</div>
        <div class="lot-detail"><b>Location:</b> &nbsp;Lorem Ipsum proin<br>Lorem Ipsum. Proin gravida nibh</div>
        <div class="lot-detail" style="margin-top:8px"><b>Begins:</b> 15-09-14 at 10:00 am CDT</div>
      </div>
    </article>

    <article class="abs auction" style="left:476px">
      <div class="auction-head">AUCTION TITLE WILL BE HERE</div>
      <div class="auction-photo" role="img" aria-label="Row of brick townhouses with a lawn and blue sky" style="background:linear-gradient(180deg,#5c95d6 0%,#a9c6e6 35%,#9a5a48 60%,#5d9a3d 100%)"></div>
      <div class="auction-btn" style="left:5px"><i></i>Details</div>
      <div class="auction-btn" style="left:85px"><i></i>Photos</div>
      <div class="auction-info">
        <div class="lot-title">4 BR / 1+ BA BRICK HOME<br>&amp; 0.630 ACRE LOT</div>
        <div class="lot-contact">DANA HOLLOWAY - ASHFORD<br>COUNTY CLERK &amp; MASTER<br>555-014-2287</div>
        <div class="bid-btn"><i></i>Click for Online Bidding</div>
        <div class="lot-live" style="margin-top:4px">LIVE ON-SITE AUCTON</div>
        <div class="lot-detail"><b>Location:</b> &nbsp;Lorem Ipsum proin<br>Lorem Ipsum. Proin gravida nibh</div>
        <div class="lot-detail" style="margin-top:5px"><b>Begins:</b> 15-09-14 at 10:00 am CDT</div>
      </div>
    </article>
  </main>

  <footer>
    <div class="abs footer"></div>
    <div class="abs content-tab"></div>
    <div class="abs partners" aria-label="Memberships">
      <span style="width:38px;height:34px;border-radius:3px"></span>
      <span style="width:22px;height:28px"></span>
      <span style="width:26px;height:26px;border-radius:50%"></span>
      <span style="width:44px;height:26px"></span>
      <span style="width:60px;height:22px;border-radius:11px"></span>
      <span style="width:48px;height:22px"></span>
    </div>

    <h3 class="abs foot-title" style="left:120px">SITE MENU</h3>
    <ul class="abs site-menu">
      <li>Home</li><li>Auctions</li><li>Services</li><li>Real Estate</li><li>Previous Auctions</li><li>About Us</li><li>Contact Us</li>
    </ul>
    <div class="abs col-divider" style="left:256px"></div>

    <h3 class="abs foot-title" style="left:309px">LATEST NEWS</h3>
    <div class="abs news" style="top:990px">
      <div class="news-photo" role="img" aria-label="Crowd at an auction event" style="background:linear-gradient(160deg,#8a6a4a,#c9b49a 50%,#4a4f6e)"></div>
      <div class="news-head">Lorem Ipsum. Proin gravida nibh</div>
      <p class="news-text">Lorem Ipsum. Proin gravida nibh vel velit auctor aliquet. Aenean sollicitudin, lorem quis</p>
    </div>
    <div class="abs news" style="top:1074px">
      <div class="news-photo" role="img" aria-label="Crowd at an auction event" style="background:linear-gradient(160deg,#8a6a4a,#c9b49a 50%,#4a4f6e)"></div>
      <div class="news-head">Lorem Ipsum. Proin gravida nibh</div>
      <p class="news-text">Lorem Ipsum. Proin gravida nibh vel velit auctor aliquet. Aenean sollicitudin, lorem quis</p>
    </div>
    <div class="abs col-divider" style="left:597px"></div>

    <h3 class="abs foot-title" style="left:657px">CONTACT INFO</h3>
    <div class="abs contact-row" style="top:987px">
      <svg width="10" height="15" viewBox="0 0 10 15"><path d="M5 0.5 A4.5 4.5 0 0 1 9.5 5 C9.5 8 5 14.5 5 14.5 C5 14.5 0.5 8 0.5 5 A4.5 4.5 0 0 1 5 0.5Z" fill="#c9cfe0"/><circle cx="5" cy="5" r="1.7" fill="#13296c"/></svg>
      <span>Lorem Ipsum. Proin gravida nibh<br>vel velit auctor aliquet. Aenean</span>
    </div>
    <div class="abs contact-row" style="top:1024px">
      <svg width="11" height="11" viewBox="0 0 11 11"><rect x="1" y="4" width="9" height="6" rx="1" fill="#c9cfe0"/><rect x="0" y="1" width="11" height="3" rx="1.5" fill="#c9cfe0"/></svg>
      <span>(017) 5550 XXX</span>
    </div>
    <div class="abs contact-row" style="top:1053px">
      <svg width="11" height="10" viewBox="0 0 11 10"><rect x="0.5" y="1.5" width="10" height="8" fill="none" stroke="#c9cfe0"/><path d="M0.5 1.5 L5.5 6 L10.5 1.5" fill="none" stroke="#c9cfe0"/></svg>
      <span>info@brevinauctions.example</span>
    </div>
    <div class="abs foot-brand"><i></i>Brevin Auctions</div>

    <div class="abs copyright-bar"></div>
    <p class="abs copyright">Copyright © 2014 Brevin Auctions, All rights reserved.</p>
  </footer>

</div>
</body>
</html>
```